Crest Path Profile Bacground Needed

I need a simple Crest Path Background graphic for my Crest Path profile. My website is www.MorvexBLD.com
I have attached a couple of photos and our logo.

The tag line is: BEAUTY | FUNCTION | ON TIME | ON BUDGET

```html
<!DOCTYPE html>
<html lang="en">
<head>
<meta charset="utf-8">
<title>Morvex Kitchen &amp; Bath – Crest Path Profile</title>
<link rel="stylesheet" href="https://fonts.googleapis.com/css2?family=Montserrat:wght@600;700&family=Roboto:wght@400;500;700&family=Tinos:wght@700&display=swap">
<style>
  :root {
    --page-bg: #ffffff;
    --frame-bg: #f2f1ee;
    --card-bg: #ffffff;
    --card-border: #e2e2df;
    --ink: #141414;
    --ink-soft: #5e5e5e;
    --tab-ink: #666666;
    --brand-blue: #0a66c2;
    --tab-active: #057642;
    --logo-tile: #f8f7f2;
    --photo-sky: #cfe6ee;
    --photo-tile: #9fbfcf;
    --photo-white: #eef2f1;
  }
  * { box-sizing: border-box; margin: 0; padding: 0; }
  html, body { width: 1200px; height: 624px; overflow: hidden; background: var(--page-bg); }
  .frame {
    position: absolute; left: 39px; top: 39px; width: 1122px; height: 546px;
    background: var(--frame-bg);
  }
  .profile-card {
    position: absolute; left: 28px; top: 28px; width: 1065px; height: 510px;
    background: var(--card-bg); border: 1px solid var(--card-border);
    border-radius: 10px; overflow: hidden;
  }
  .banner { position: absolute; left: 0; top: 0; width: 100%; height: 180px; }
  .banner-photo {
    position: absolute; inset: 0;
    background:
      linear-gradient(180deg, rgba(207,230,238,0.9) 0%, rgba(169,194,122,0.55) 38%, rgba(238,242,241,0.9) 62%, rgba(159,191,207,0.7) 100%),
      linear-gradient(90deg, var(--photo-tile) 0%, var(--photo-white) 22%, var(--photo-sky) 50%, var(--photo-white) 78%, var(--photo-tile) 100%);
  }
  .brand-name {
    display: flex; align-items: center; gap: 10px;
    font-family: "Montserrat", sans-serif; font-weight: 600; color: var(--ink);
  }
  .brand-square { flex: none; background: var(--ink); }
  .banner-brand {
    position: absolute; left: 0; width: 100%; top: 56px;
    justify-content: center; padding-left: 6px;
    font-size: 30px; line-height: 1;
  }
  .banner-brand .brand-square { width: 16px; height: 16px; }
  .tagline {
    position: absolute; left: 0; width: 100%; top: 143px; text-align: center;
    padding-left: 12px;
    font-family: "Tinos", serif; font-weight: 700; font-size: 13px; letter-spacing: 0.4px;
    color: #2a2a2a;
  }
  .logo-tile {
    position: absolute; left: 32px; top: 94px; width: 170px; height: 164px;
    background: var(--logo-tile);
    display: flex; align-items: center; justify-content: center;
  }
  .logo-tile .brand-name { font-size: 17px; line-height: 1.25; gap: 8px; width: 130px; }
  .logo-tile .brand-square { width: 10px; height: 10px; }
  .company-name {
    position: absolute; left: 29px; top: 282px;
    font-family: "Montserrat", sans-serif; font-weight: 700; font-size: 32px; color: var(--ink);
  }
  .company-meta {
    position: absolute; left: 29px; top: 321px;
    font-family: "Roboto", sans-serif; font-size: 20px; color: var(--ink-soft);
  }
  .actions { position: absolute; left: 32px; top: 368px; display: flex; gap: 11px; align-items: center; }
  .btn {
    height: 42px; width: 178px; border-radius: 21px;
    display: flex; align-items: center; justify-content: center; gap: 10px;
    font-family: "Roboto", sans-serif; font-weight: 500; font-size: 21px;
  }
  .btn-follow { background: var(--brand-blue); color: #fff; }
  .btn-message { border: 1.5px solid var(--brand-blue); color: var(--brand-blue); background: #fff; }
  .btn-more {
    width: 42px; height: 42px; border-radius: 50%; border: 1.5px solid #444;
    display: flex; align-items: center; justify-content: center; margin-left: 1px;
  }
  .tabs {
    position: absolute; left: 0; top: 442px; width: 100%; height: 68px;
    border-top: 1px solid var(--card-border);
    display: flex; padding-left: 26px;
    font-family: "Roboto", sans-serif; font-weight: 500; font-size: 21px;
  }
  .tab { color: var(--tab-ink); padding-top: 21px; margin-right: 42px; position: relative; height: 68px; }
  .tab-active { color: var(--tab-active); font-weight: 700; }
  .tab-active::after {
    content: ""; position: absolute; left: -21px; right: -21px; bottom: 0; height: 3px; background: var(--tab-active);
  }
</style>
</head>
<body>
  <div class="frame">
    <div class="profile-card">
      <header class="banner">
        <div class="banner-photo" role="img" aria-label="Photo of a bright coastal bathroom with blue tile, white vanities, a freestanding tub and ocean-view windows"></div>
        <div class="brand-name banner-brand">
          <span class="brand-square"></span>
          <span>Morvex Kitchen &amp; Bath</span>
        </div>
        <p class="tagline">BEAUTY | FUNCTION | ON TIME | ON BUDGET</p>
      </header>

      <div class="logo-tile">
        <div class="brand-name">
          <span class="brand-square"></span>
          <span>Morvex Kitchen &amp; Bath</span>
        </div>
      </div>

      <h1 class="company-name">Morvex, KITCHEN &amp; BATH</h1>
      <p class="company-meta">Kitchen Remodeling, Bathroom Remodeling &bull; Charlotte NC Region</p>

      <div class="actions">
        <div class="btn btn-follow">
          <svg width="18" height="18" viewBox="0 0 18 18"><path d="M9 1v16M1 9h16" stroke="#fff" stroke-width="2.4"/></svg>
          Follow
        </div>
        <div class="btn btn-message">
          <svg width="20" height="20" viewBox="0 0 20 20"><path d="M19 1 1 8l7 3 3 8z" fill="#0a66c2"/></svg>
          Message
        </div>
        <div class="btn-more">
          <svg width="20" height="6" viewBox="0 0 20 6"><circle cx="3" cy="3" r="2" fill="#333"/><circle cx="10" cy="3" r="2" fill="#333"/><circle cx="17" cy="3" r="2" fill="#333"/></svg>
        </div>
      </div>

      <nav class="tabs">
        <span class="tab">Home</span>
        <span class="tab">About</span>
        <span class="tab tab-active">Posts</span>
        <span class="tab">Jobs</span>
        <span class="tab">People</span>
      </nav>
    </div>
  </div>
</body>
</html>
```